Brightmore Machinery Forklift rental website

I'm seeking a proficient web developer to build a forklift rental website tailored to large warehouses. I am not looking for a generic site, I want it to be attractive and sleek to potential customers. I have attached my logo to give a better idea about my design preferences .
The site must encompass various functionalities: - A rental booking system to allow customers reserve forklifts seamlessly, making the rental process simpler. - An inventory management system that offers real-time tracking of our diverse range of forklifts including Electric forklifts, Reach trucks, Order pickers, Sit and Stand up counterbalances, Swing reach, Propane sit down counterbalances and chargers. For each forklift listed, the site should display explicit specifications, current rental rates, and an availability calendar to aid customers in making informed rental decisions. Ideal skills for this role will include web development, experience in building booking and potentially some knowledge of the renting industry, although this is not essential. Experience in creating inventory management systems is also looked upon favorably. I would also like a section that I can list forklifts for sale. Preferably the website would be designed to convert into an app as well. The website will need a payment portal that can accept credit cards, ach payments and possibly e-check/ wire transfer.
Most bookings will be monthly so I need a system that can accommodate that. I will also need an option to leave the bookings open ended in the event the customer wants to keep the unit until further notice.
Target Market(s)
Industrial warehouses
Coding
Coded - Design and coding required
Number of Pages Required
1 page
Look and feel
Each slider illustrates characteristics of the customer's brand and the style your logo design should communicate.

```html
<!DOCTYPE html>
<html lang="en">
<head>
<meta charset="utf-8">
<title>Brightmore Machinery – Forklift Rental</title>
<link rel="stylesheet" href="https://fonts.googleapis.com/css2?family=Exo:wght@400;500;700;800&display=swap">
<style>
  :root {
    --red: #b20e06;
    --red-soft: #b8342c;
    --navy: #1f2d6b;
    --white: #ffffff;
    --search-grey: #d8d6d6;
    --stage: #e6e5e7;
    --font: "Exo", sans-serif;
  }
  * { box-sizing: border-box; margin: 0; padding: 0; }
  html, body { width: 1200px; height: 1200px; overflow: hidden; }
  body { background: var(--stage); font-family: var(--font); position: relative; }

  .site { position: absolute; left: 0; top: 262px; width: 1200px; height: 676px; background: var(--white); overflow: hidden; }

  .hero { position: absolute; left: 0; top: 0; width: 1200px; height: 392px;
    background: linear-gradient(90deg, var(--red) 0%, var(--red) 60%, #b4251b 72%, var(--red-soft) 80%); }
  .hero-photo { position: absolute; left: 809px; top: 0; width: 391px; height: 392px;
    background: linear-gradient(180deg, #8a5f4a 0%, #6b5247 30%, #4a3d3d 55%, #9a9490 78%, #b7b3ae 100%); }

  .brand { position: absolute; left: 119px; top: 39px; display: flex; align-items: center; gap: 7px;
    color: var(--white); font-weight: 800; font-size: 15px; letter-spacing: 0.5px; text-transform: uppercase; }
  .brand-mark { width: 12px; height: 12px; background: var(--white); }

  .search { position: absolute; left: 384px; top: 46px; width: 433px; height: 21px; border-radius: 11px;
    background: var(--search-grey); display: flex; align-items: center; justify-content: space-between; padding: 0 8px 0 10px; }
  .search-label { font-size: 12px; color: #ffffff; letter-spacing: 0.4px; }
  .search-icon { width: 18px; height: 14px; }

  .call-pill { position: absolute; left: 853px; top: 46px; width: 188px; height: 20px; border-radius: 10px;
    background: var(--red); color: var(--white); font-size: 13px; letter-spacing: 0.5px;
    display: flex; align-items: center; justify-content: center; }
  .call-pill strong { font-weight: 800; margin-right: 5px; }

  .hero-title { position: absolute; left: 112px; top: 126px; color: var(--white); font-weight: 800;
    font-size: 46px; line-height: 50px; letter-spacing: 2.5px; text-transform: uppercase; }
  .hero-text { position: absolute; left: 112px; top: 227px; width: 570px; color: var(--white);
    font-size: 15.5px; line-height: 18px; letter-spacing: 0.9px; }

  .btn { position: absolute; top: 320px; height: 28px; font-size: 13px; letter-spacing: 0.8px; color: var(--white);
    display: flex; align-items: center; justify-content: center; }
  .btn-primary { left: 112px; width: 120px; background: var(--navy); }
  .btn-outline { left: 250px; width: 124px; border: 2px solid var(--navy); }

  .section-title { position: absolute; left: 112px; color: var(--navy); font-weight: 800; font-size: 22px;
    letter-spacing: 0.8px; padding-left: 8px; border-left: 2px solid var(--red); line-height: 24px; }
  .about-title { top: 410px; }
  .about-text { position: absolute; left: 112px; top: 443px; width: 600px; color: var(--navy);
    font-size: 8.6px; line-height: 10.1px; letter-spacing: 0.35px; }

  .about-photo { position: absolute; top: 412px; width: 205px; height: 185px; }
  .about-photo.one { left: 746px; background: linear-gradient(180deg, #8f8d88 0%, #c9c6c0 40%, #a8a29a 75%, #7d776f 100%); }
  .about-photo.two { left: 959px; background: linear-gradient(180deg, #b8ad97 0%, #d7cdb5 45%, #8f8577 78%, #6f685e 100%); }

  .fleet-title { top: 603px; }
  .fleet-list { position: absolute; left: 121px; top: 632px; list-style: none; color: var(--navy);
    font-size: 14.5px; line-height: 12.7px; letter-spacing: 1px; }
  .fleet-list li { display: flex; align-items: center; gap: 9px; }
  .fleet-list li::before { content: ""; width: 7px; height: 7px; background: var(--red); transform: rotate(45deg); }
</style>
</head>
<body>
  <main class="site">
    <header class="hero">
      <div class="hero-photo" role="img" aria-label="Photo of a red reach truck forklift in a warehouse aisle with tall pallet racking"></div>

      <div class="brand"><span class="brand-mark"></span>Brightmore Machinery</div>

      <div class="search">
        <span class="search-label">Search</span>
        <svg class="search-icon" viewBox="0 0 18 14" aria-hidden="true">
          <circle cx="8" cy="6" r="4.6" fill="none" stroke="#1f2d6b" stroke-width="1.4"/>
          <line x1="11.4" y1="9.2" x2="15.5" y2="12.6" stroke="#1f2d6b" stroke-width="1.6" stroke-linecap="round"/>
        </svg>
      </div>

      <div class="call-pill"><strong>Call Us</strong>+000 111 222 333</div>

      <h1 class="hero-title">Our Service Built<br>Our Company</h1>
      <p class="hero-text">is simply dummy text of the printing and typesetting industry. Lorem Ipsum has been the industry's standard dummy text ever since the 1500s, when an unknown printer took a galley of type</p>

      <a class="btn btn-primary"></a>
      <a class="btn btn-outline">Clients</a>
    </header>

    <section>
      <h2 class="section-title about-title">Who Are we</h2>
      <p class="about-text">is simply dummy text of the printing and typesetting industry. Lorem Ipsum has been the industry's standard dummy text ever since the 1500s, when an unknown printer took a galley of type is simply dummy text of the printing and type-setting industry. Lorem Ipsum has been the industry's standard dummy text ever since the 1500s, when an unknown printer took a galley of type<br>is simply dummy text of the printing and typesetting industry. Lorem Ipsum has been the industry's standard dummy text ever since the 1500s, when an unknown printer took a galley of type is simply dummy text of the printing and type-setting industry. Lorem Ipsum has been the industry's standard dummy text ever since the 1500s, when an unknown printer took a galley of type is simply dummy text of the printing and typesetting industry. Lorem Ipsum has been the industry's standard dummy text ever since the 1500s, when an unknown printer took a galley of type<br>is simply dummy text of the printing and typesetting industry. Lorem Ipsum has been the industry's standard dummy text ever since the 1500s, when an unknown printer took a galley of type</p>
      <div class="about-photo one" role="img" aria-label="Photo of a red reach truck forklift parked at a charging station beside a traffic cone"></div>
      <div class="about-photo two" role="img" aria-label="Photo of a red forklift in a warehouse bay next to a charger and traffic cone"></div>
    </section>

    <section>
      <h2 class="section-title fleet-title">Our Forklifts</h2>
      <ul class="fleet-list">
        <li>Learn&nbsp; moremore</li>
        <li>Dummy text of</li>
        <li>When an unknown</li>
      </ul>
    </section>
  </main>
</body>
</html>
```